2018 Desk Calendar Design with Better Spine, Better Health with Chiropractic

In conjunction with the Federation of Vertebral Wellness Malaysia (FVW), we are organizing a 2018 desk calendar design. The cover page and monthly design size is 210mm (H) x 195mm (W). The will be a total of 27 designs including a cover page (front) [Sample 1], cover page (back) Malaysia National & States Holiday 2018 (https://calendaroffdays.com.my/2018-dates/) [Sample 2], 12 months design (front) [Sample 3 and 4], 12 months design (back) [Sample 5], Last page (2017 and 2019 calendar) [Sample 6].

Below are some recommendations for monthly back cover design. The main theme remain as Better SPINE, Better HEALTH with CHIROPRACTIC. Each month can in collaborate with of the following element:-

Suggestion 1 (Celebration of the Month)
January - New Year
February - Chinese New Year
March -
April -
May - Labour Day
June - Aidilfitri Festival
July-
August - Independent Day
September - Malaysia Day
October - Global Posture Week
November - Deepavali Festival
December - Christmas

Suggestion 2 (States in Malaysia)
January - Perlis
February - Kedah
March - Penang
April - Perak
May - Selangor
June - Negeri Sembilan
July- Melaka
August - Johor
September - Pahang
October - Terengganu
November - Kelantan
December - Sabah & Sarawak

Reason: Looking forward to receive all the designs.

Target Market(s)

Chiropractors and Public

Industry/Entity Type

Chiropractor

Colors

Designer to choose colors to be used in the design.

Requirements
Must have
• The theme for the desk calendar design is Better Spine, Better Health with Chiropractic.
• The cover page should include 5th Anniversary element.
Nice to have
• Lunar or Islamic calendar is optional in the Gregorian calendar.
• AI Format
• Footnote of each page www.vertifvw.org

```html
<!DOCTYPE html>
<html lang="en">
<head>
<meta charset="utf-8">
<title>January 2018 – Desk Calendar</title>
<link rel="stylesheet" href="https://fonts.googleapis.com/css2?family=Alex+Brush&family=Arimo:ital,wght@0,400;0,700;1,400&display=swap">
<style>
  :root{
    --navy:#2e3192;
    --blue:#2b3aa0;
    --red:#e0202a;
    --ink:#111111;
    --grey-col:#e4e4e4;
    --rule:#8e8e8e;
    --yellow:#fde428;
    --purple:#54479a;
    --white:#ffffff;
  }
  *{margin:0;padding:0;box-sizing:border-box}
  html,body{width:1200px;height:1115px;overflow:hidden;background:var(--white)}
  body{font-family:"Arimo",Arial,sans-serif;color:var(--ink)}
  .page{position:relative;width:1200px;height:1115px}

  .binding{position:absolute;left:0;top:10px;width:1200px;height:26px;display:flex;gap:16px;padding-left:8px}
  .binding span{width:24px;height:24px;background:var(--ink);flex:none}

  .photo{position:absolute;left:0;top:56px;width:464px;height:1034px;
    background:linear-gradient(180deg,#f3ece6 0%,#d9b49a 22%,#ead9cc 45%,#f2c46a 62%,#e77a2c 78%,#7f9a3c 92%);}

  .tagline{position:absolute;left:0;top:826px;width:456px;height:264px;
    background:linear-gradient(180deg,rgba(84,71,154,.88),rgba(74,60,140,.95));
    color:var(--white);font-style:italic;font-size:26.5px;line-height:31px;padding:20px 14px 0 14px}

  .month-head{position:absolute;left:476px;top:52px;width:590px;height:150px}
  .month-name{position:absolute;left:0;top:0;font-family:"Alex Brush",cursive;font-size:108px;color:var(--navy);line-height:1}
  .month-year{position:absolute;right:0;top:34px;font-size:66px;color:var(--navy);line-height:1}
  .month-rule{position:absolute;left:264px;top:106px;width:326px;height:3px;background:var(--navy)}

  .grid{position:absolute;left:466px;top:230px;width:706px;height:414px;display:grid;
    grid-template-columns:repeat(7,1fr);grid-template-rows:26px repeat(5,1fr);column-gap:4px}
  .grid .weekend{background:var(--grey-col)}
  .dow{font-weight:700;font-size:22px;color:var(--blue);padding-left:4px;border-top:2px solid #cfcfcf}
  .day{font-weight:700;font-size:27px;padding:8px 0 0 8px;border-bottom:3px solid var(--rule)}
  .day.last{border-bottom:none}
  .day.holiday{color:var(--red)}

  .mini{position:absolute;top:664px;width:138px;font-size:10.5px}
  .mini h3{font-size:11px;font-weight:400;color:var(--navy);text-align:center;margin-bottom:4px}
  .mini .cells{display:grid;grid-template-columns:repeat(7,1fr);row-gap:3px}
  .mini .cells span{text-align:center;height:14px;line-height:14px}
  .mini .cells .hd{font-weight:700}
  .mini .cells .we{background:var(--grey-col)}
  .mini-dec{left:610px}
  .mini-feb{left:834px}

  .holidays-title{position:absolute;left:474px;top:840px;width:698px;display:flex;align-items:center;gap:14px;color:var(--red);font-size:25px}
  .holidays-title::before,.holidays-title::after{content:"";flex:1;height:2px;background:var(--red)}
  .holiday-list{position:absolute;top:880px;font-size:14px;line-height:30px;list-style:none}
  .holiday-list b{color:var(--ink);margin-right:8px}
  .holiday-list span{color:var(--red)}
  .holiday-list.left{left:466px}
  .holiday-list.right{left:864px}

  .org{position:absolute;left:456px;top:966px;width:714px;height:124px;background:var(--yellow);padding:8px 0 0 16px;color:var(--navy)}
  .org-name{font-weight:700;font-size:24px;line-height:28px}
  .org-name-local{font-size:19px;line-height:24px}
  .org-contact-label{font-weight:700;font-size:17px;line-height:22px;color:var(--ink)}
  .org-contact{font-size:26px;line-height:28px;color:var(--ink)}
  .org-contact .sep{margin:0 22px}
  .org-mark{position:absolute;right:14px;top:26px;display:flex;align-items:center;gap:8px;font-weight:700;font-size:28px;color:var(--navy)}
  .org-mark i{display:block;width:22px;height:22px;border-radius:50%;background:var(--navy)}
</style>
</head>
<body>
<div class="page">
  <div class="binding" aria-hidden="true">
    <span></span><span></span><span></span><span></span><span></span><span></span><span></span><span></span><span></span><span></span><span></span><span></span><span></span><span></span><span></span><span></span><span></span><span></span><span></span><span></span><span></span><span></span><span></span><span></span><span></span><span></span><span></span><span></span><span></span>
  </div>

  <div class="photo" role="img" aria-label="Photo of a smiling woman in sportswear holding a glass of orange juice and giving a thumbs up, with fresh fruit and vegetables in front"></div>

  <p class="tagline">Chiropractic is a healthcare discipline that emphasizes the inherent recuperative power of the body to heal itself &nbsp;without the use of drugs or surgery.</p>

  <header class="month-head">
    <h1 class="month-name">January</h1>
    <div class="month-rule"></div>
    <div class="month-year">2018</div>
  </header>

  <section class="grid" aria-label="January 2018">
    <div class="dow weekend">Sun</div><div class="dow">Mon</div><div class="dow">Tue</div><div class="dow">Wed</div><div class="dow">Thu</div><div class="dow">Fri</div><div class="dow weekend">Sat</div>

    <div class="day weekend"></div><div class="day holiday">1</div><div class="day">2</div><div class="day">3</div><div class="day">4</div><div class="day">5</div><div class="day weekend">6</div>
    <div class="day weekend">7</div><div class="day">8</div><div class="day">9</div><div class="day">10</div><div class="day">11</div><div class="day">12</div><div class="day weekend">13</div>
    <div class="day weekend holiday">14</div><div class="day">15</div><div class="day">16</div><div class="day">17</div><div class="day">18</div><div class="day">19</div><div class="day weekend">20</div>
    <div class="day weekend holiday">21</div><div class="day">22</div><div class="day">23</div><div class="day">24</div><div class="day">25</div><div class="day">26</div><div class="day weekend">27</div>
    <div class="day last weekend">28</div><div class="day last">29</div><div class="day last">30</div><div class="day last holiday">31</div><div class="day last"></div><div class="day last"></div><div class="day last weekend"></div>
  </section>

  <section class="mini mini-dec">
    <h3>December 2017</h3>
    <div class="cells">
      <span class="hd">S</span><span class="hd">M</span><span class="hd">T</span><span class="hd">W</span><span class="hd">T</span><span class="hd">F</span><span class="hd">S</span>
      <span class="we"></span><span></span><span></span><span></span><span></span><span>1</span><span class="we">2</span>
      <span class="we">3</span><span>4</span><span>5</span><span>6</span><span>7</span><span>8</span><span class="we">9</span>
      <span class="we">10</span><span>11</span><span>12</span><span>13</span><span>14</span><span>15</span><span class="we">16</span>
      <span class="we">17</span><span>18</span><span>19</span><span>20</span><span>21</span><span>22</span><span class="we">23</span>
      <span class="we">24</span><span>25</span><span>26</span><span>27</span><span>28</span><span>29</span><span class="we">30</span>
      <span class="we">31</span>
    </div>
  </section>

  <section class="mini mini-feb">
    <h3>February 2018</h3>
    <div class="cells">
      <span class="hd">S</span><span class="hd">M</span><span class="hd">T</span><span class="hd">W</span><span class="hd">T</span><span class="hd">F</span><span class="hd">S</span>
      <span class="we"></span><span></span><span></span><span></span><span>1</span><span>2</span><span class="we">3</span>
      <span class="we">4</span><span>5</span><span>6</span><span>7</span><span>8</span><span>9</span><span class="we">10</span>
      <span class="we">11</span><span>12</span><span>13</span><span>14</span><span>15</span><span>16</span><span class="we">17</span>
      <span class="we">18</span><span>19</span><span>20</span><span>21</span><span>22</span><span>23</span><span class="we">24</span>
      <span class="we">25</span><span>26</span><span>27</span><span>28</span>
    </div>
  </section>

  <h2 class="holidays-title">Holidays</h2>
  <ul class="holiday-list left">
    <li><b>1 Jan</b><span>New Year's Day</span></li>
    <li><b>14 Jan</b><span>YDPB Negeri Sembilan's Birthday</span></li>
  </ul>
  <ul class="holiday-list right">
    <li><b>21 Jan</b><span>Sultan of Kedah's Birthday</span></li>
    <li><b>31 Jan</b><span>Thaipusam</span></li>
  </ul>

  <footer class="org">
    <div class="org-name">Federation of Vertebral Wellness Malaysia</div>
    <div class="org-name-local">Persekutuan Kesihatan Vertebra Malaysia</div>
    <div class="org-contact-label">email:</div>
    <div class="org-contact">enquiry@vertifvw.org<span class="sep">|</span>www.vertifvw.org</div>
    <div class="org-mark"><i></i>FVW</div>
  </footer>
</div>
</body>
</html>
```